Chic streamline modern edgy! Tamvexcurl.com

I need a website built for my personal business. I am a hair stylist and I would like a crisp website that works well, is sleek, easy to use, and allows my clients to navigate through Services and pay deposits for services listed.

My logo is somewhat of a full moon, so my theme is nocturnal.

My information can be found at bookmiro.com/tamvexcurl

Target Market(s)

Women ages 25-55 who are looking for luxury hair extension services

Industry/Entity Type

Hair And Beauty

Number of Pages Required

1 page

Colors
474747
919191
d3d3d3
000000

Requirements
Must have
• Location map, quorba link embedded for deposits, contact box, bio, faq/policies, menu of services, hours of availability by appointment only .
Nice to have
• An interactive calander where I could post dates that I am available, preferred providers for other beauty services where i could list other websites for make up and other beauty related referrals. a bridal tab would be nice to offer information about bridal services and policies.

```html
<!DOCTYPE html>
<html lang="en">
<head>
<meta charset="utf-8">
<title>Tamvex Curl — Hair</title>
<link rel="stylesheet" href="https://fonts.googleapis.com/css2?family=Barlow:wght@300;400;500;600&display=swap">
<style>
:root{
  --black:#000000;
  --charcoal:#474747;
  --steel:#919191;
  --silver:#d3d3d3;
  --card:#1e1e1e;
  --band:#222222;
  --bar:#2b2b2b;
  --red:#c40f0f;
  --white:#ffffff;
}
*{box-sizing:border-box;margin:0;padding:0}
html,body{width:1200px;height:2773px;overflow:hidden;background:var(--black)}
body{position:relative;font-family:"Barlow",Arial,sans-serif;color:var(--white)}
.abs{position:absolute}

/* hero */
.hero{left:0;top:0;width:1200px;height:717px;background:var(--black)}
.hero-photo{left:407px;top:0;width:793px;height:717px;
  background:radial-gradient(ellipse at 62% 28%,#9a9a9a 0%,#4d4d4d 30%,#1c1c1c 62%,#000 100%)}
.brand-moon{left:144px;top:107px;width:156px;height:156px;border-radius:50%;background:var(--silver)}
.brand-name{left:40px;top:282px;width:364px;text-align:center;font-weight:300;font-size:44px;letter-spacing:5px;color:var(--white)}
.main-nav{left:103px;top:404px;width:300px;text-align:center;list-style:none}
.main-nav li{font-size:21px;line-height:25px;color:var(--steel);font-weight:400}
.pay-mark{left:1024px;top:642px;display:flex;align-items:center;gap:10px;font-weight:600;font-size:28px;color:var(--white)}
.pay-mark span.dot{width:22px;height:22px;border-radius:50%;background:var(--white)}

/* about band */
.about{left:0;top:717px;width:1200px;height:531px;background:linear-gradient(180deg,#5b5b5b 0%,#444 100%)}
.bio-photo{left:0;top:4px;width:403px;height:301px;background:linear-gradient(135deg,#8a8a8a 0%,#5a5a5a 55%,#3a3a3a 100%)}
.hours{left:0;top:305px;width:403px;height:226px;background:#5c5c5c;padding:58px 0 0 59px;color:#b5b5b5}
.hours h3{font-weight:400;font-size:16px;color:var(--silver);margin-bottom:10px}
.hours table{border-collapse:collapse;font-size:15px}
.hours td{height:18.5px;padding:0}
.hours td.day{width:94px}.hours td.open{width:86px}.hours td.dash{width:46px}
.bio{left:438px;top:60px;width:500px}
.bio h2{font-weight:400;font-size:20px;margin-bottom:8px}
.bio p{font-size:11.5px;line-height:13px;color:var(--silver)}
.calendar{left:989px;top:30px;width:168px}
.cal-head{display:flex;justify-content:space-between;font-size:12px;color:var(--silver);padding:0 8px 6px}
.cal-grid{background:#1a1a1a;border:2px solid #777;border-collapse:collapse;width:168px}
.cal-grid th{font-size:8px;font-weight:400;color:var(--steel);height:14px}
.cal-grid td{font-size:10px;text-align:center;height:22px;color:var(--white)}
.cal-grid td.mute{color:#666}
.cal-grid td.pick span{background:#777;padding:2px 4px}
.cal-grid td.open span{display:inline-block;width:17px;height:17px;line-height:17px;border-radius:50%;background:var(--red)}
.cal-key{font-size:9px;color:var(--silver);margin-top:6px;display:flex;align-items:center;gap:4px}
.cal-key i{width:9px;height:7px;background:var(--red);display:inline-block}
.map{left:405px;top:228px;width:795px;height:303px;background:linear-gradient(160deg,#ecebe7 0%,#e2e0da 100%)}
.map-pin{left:785px;top:1066px}

/* services */
.services-title{left:0;top:1308px;width:1200px;text-align:center;font-size:26px;font-weight:400}
.group-label{font-size:11.5px;font-weight:500;letter-spacing:.3px}
.card{width:331px;height:233px;background:var(--card);padding:30px 26px 0 26px}
.card h3{font-weight:400;font-size:26px;margin-bottom:14px}
.card p{font-size:12.5px;line-height:15px;color:var(--silver);height:62px}
.card .price{position:absolute;left:26px;top:150px;font-size:25px;line-height:29px}
.card .book{position:absolute;right:13px;top:180px;width:102px;height:40px;background:var(--red);color:var(--white);font-size:18px;text-align:center;line-height:40px;letter-spacing:.5px}

/* testimonial */
.review{left:0;top:2335px;width:1200px;height:244px;background:var(--band)}
.review-name{right:723px;top:76px;font-size:33px;color:var(--steel);text-align:right}
.review-date{right:777px;top:142px;font-size:20px;color:var(--silver)}
.review-quote{left:499px;top:72px;width:520px;font-size:18px;line-height:20px;color:#6b6b6b}

/* footer */
.footer-nav{left:40px;top:2617px;font-size:17px;color:var(--white)}
.social{top:2607px;display:flex;gap:14px;left:966px}
.social span{width:54px;height:54px;border-radius:50%;background:#cfcfcf;color:#111;font-size:12px;font-weight:500;display:flex;align-items:center;justify-content:center}
.base{left:0;top:2690px;width:1200px;height:83px;background:var(--bar);font-size:14px;color:#777}
.base .addr{left:37px;top:30px}
.base .rights{right:26px;top:30px}
</style>
</head>
<body>

<header class="hero abs">
  <div class="hero-photo abs" role="img" aria-label="Black and white portrait of a model with long sleek straight hair"></div>
  <div class="brand-moon abs"></div>
  <div class="brand-name abs">TAMVEX CURL</div>
  <ul class="main-nav abs">
    <li>Biography</li><li>Contact</li><li>Calendar</li><li>Services</li><li>Book an Appointment</li><li>FAQ</li>
  </ul>
  <div class="pay-mark abs"><span class="dot"></span>quorba</div>
</header>

<section class="about abs">
  <div class="bio-photo abs" role="img" aria-label="Portrait photo of the stylist"></div>
  <div class="hours abs">
    <h3>Business Hours</h3>
    <table>
      <tr><td class="day">Tuesday</td><td class="open">7:00am</td><td class="dash">—</td><td>7:00pm</td></tr>
      <tr><td class="day">Wednesday</td><td class="open">7:00am</td><td class="dash">—</td><td>7:00pm</td></tr>
      <tr><td class="day">Thursday</td><td class="open">7:00am</td><td class="dash">—</td><td>7:00pm</td></tr>
      <tr><td class="day">Friday</td><td class="open">7:00am</td><td class="dash">—</td><td>7:00pm</td></tr>
      <tr><td class="day">Saturday</td><td class="open">7:00am</td><td class="dash">—</td><td>7:00pm</td></tr>
    </table>
  </div>
  <div class="bio abs">
    <h2>Biography</h2>
    <p>Professional Hair Stylist, Tam Vexley, has devised a signature approach to Hair Design.<br>
    Tam studied the science of beautiful hair at Corvane Academy in his native city of Fairbrook Texas.<br>
    He continues to sharpen his skill set with continued color and cutting education from Orlen Studio,<br>
    Kestrine, and Mavoli. His love for healthy hair care is emphasized by his ability to create<br>
    undetectable extensions. These additions not only accentuate his clients appearance,<br>
    they promote growth and protection of their natural mane. To further his artistic technique,<br>
    Tam travels to international hair shows and and events in the states and abroad.</p>
  </div>
  <div class="calendar abs">
    <div class="cal-head"><span>&lt;</span><span>APRIL 2016</span><span>&gt;</span></div>
    <table class="cal-grid">
      <tr><th>sun</th><th>mon</th><th>tue</th><th>wed</th><th>thu</th><th>fri</th><th>sat</th></tr>
      <tr><td class="mute">31</td><td>1</td><td class="pick"><span>2</span></td><td>3</td><td>4</td><td>5</td><td>6</td></tr>
      <tr><td>7</td><td>8</td><td>9</td><td class="open"><span>10</span></td><td class="open"><span>11</span></td><td class="open"><span>12</span></td><td>13</td></tr>
      <tr><td>14</td><td>15</td><td class="open"><span>16</span></td><td>17</td><td class="open"><span>18</span></td><td>19</td><td>20</td></tr>
      <tr><td>21</td><td>22</td><td>23</td><td class="open"><span>24</span></td><td>25</td><td>26</td><td>27</td></tr>
      <tr><td>28</td><td>29</td><td>30</td><td>31</td><td class="mute">1</td><td class="mute">2</td><td class="mute">3</td></tr>
    </table>
    <div class="cal-key"><i></i>AVAILABLE</div>
  </div>
  <div class="map abs" role="img" aria-label="Street map showing the salon location"></div>
</section>
<svg class="map-pin abs" width="20" height="28" viewBox="0 0 20 28" aria-hidden="true"><path d="M10 0C4.5 0 0 4.4 0 9.8 0 17 10 28 10 28s10-11 10-18.2C20 4.4 15.5 0 10 0z" fill="#d12b2b"/><circle cx="10" cy="10" r="3.5" fill="#7a1010"/></svg>

<h2 class="services-title abs">Services and Book an Appointment</h2>

<div class="group-label abs" style="left:70px;top:1379px">ADJUSTMENTS</div>
<div class="group-label abs" style="left:806px;top:1379px">ARRANGEMENTS</div>
<div class="group-label abs" style="left:70px;top:1687px">ATTACHMENTS</div>
<div class="group-label abs" style="left:437px;top:1687px">ENHANCEMENTS</div>
<div class="group-label abs" style="left:806px;top:1687px">UPGRADES</div>

<article class="card abs" style="left:68px;top:1413px"><h3>Relaxer</h3><p>For current clients Sorelle Relaxer used.<br>Deep Conditioning treatment and trim included.<br>Addition fee may be required depending<br>on the ... [more]</p><div class="price">$100 and up<br>2 hr.</div><div class="book">REQUEST</div></article>
<article class="card abs" style="left:435px;top:1413px"><h3>Extension removal</h3><p>Removal of sewn in extensions.<br>Wash, Deep condition, trim, and natural hair<br>assessment are included (this service is ideal<br>for ... [more]</p><div class="price">$85 and up<br>1 hr., 45 min.</div><div class="book">REQUEST</div></article>
<article class="card abs" style="left:802px;top:1413px;padding-top:26px"><h3>Consultation</h3><p>Hair consultations can be crucial and necessary f<br>or new Clients. This is a perfect way for me<br>to gauge your ... [more]</p><div class="price" style="top:150px">$55<br>15 min.</div><div class="book">REQUEST</div></article>

<article class="card abs" style="left:68px;top:1721px"><h3>Extensions</h3><p>Extensions, done correctly, are a great way<br>to protect and grow your natural hair. Using<br>a braiding technique that prevents ... [more]</p><div class="price">$275 and up<br>3 hr.</div><div class="book">REQUEST</div></article>
<article class="card abs" style="left:435px;top:1721px"><h3>Color services</h3><p>In person consultation required for new clients<br>Single process color involves the application<br>of permanent, semi-permanent or demi-<br>permanent color to ... [more]</p><div class="price">$125 and up<br>2 hr.</div><div class="book">REQUEST</div></article>
<article class="card abs" style="left:802px;top:1721px"><h3>Extension Straightening</h3><p>For extremely curly extension clients who desire<br>a bone straight look or a curl that is looser<br>than the natural ... [more]</p><div class="price">$50 and up<br>45 min.</div><div class="book">REQUEST</div></article>

<article class="card abs" style="left:68px;top:2034px"><h3>Hair Cut</h3><p>Ready for a new look? This service is commonly<br>paired with a shampoo set , great for pre-existing<br>extensions and ... [more]</p><div class="price">$35 and up<br>45 min.</div><div class="book">REQUEST</div></article>
<article class="card abs" style="left:435px;top:2034px"><h3>Specialty Curls</h3><p>Wand Curls</p><div class="price">$25 and up<br>1 hr.</div><div class="book">REQUEST</div></article>
<article class="card abs" style="left:802px;top:2034px;padding-top:24px"><h3>specialty styles</h3><p>Updo styling ideal for special events.</p><div class="price" style="top:138px">$55 and up<br>45 min.</div><div class="book">REQUEST</div></article>

<section class="review abs">
  <div class="review-name abs">Marisol K.</div>
  <div class="review-date abs">7/30/15</div>
  <blockquote class="review-quote abs">"I will not let anyone sew in my hair but Tam...<br>His braiding foundation is everything!!!! He is so sweet<br>and you are truly entertained in his shop..I love Tam Vexley!<br>Definitely book your next appointment here!"</blockquote>
</section>

<nav class="footer-nav abs">HOME | Contact and Biography | Calendar | Services and Book an Appointment | FAQ |</nav>
<div class="social abs"><span>Kivo</span><span>Pelt</span><span>Lumo</span></div>

<footer class="base abs">
  <div class="addr abs">Address : Lumen Salon Suite 4410 Harrow Lane 7 Fairbrook, TX &nbsp;&nbsp; 555-013-2740</div>
  <div class="rights abs">© 2016 &nbsp;Tamvexcurl.com. All rights reserved.</div>
</footer>

</body>
</html>
```